Lomi-Seret - Promote and Support a community

Design a website for Ethiopean Community. the design should be friendly, easy to navigate and maintain the look & feel of the Ethiopian culture. a proposed logo is attached but it can be change according to your recommendations. This is a project we are doing at a discount rate as it supports a weak community.
Please visit their current website http://www.lomi-seret.example.il/index.php?lang=en

Target Market(s)

Community members, potential doners

Industry/Entity Type

community

Number of Pages Required

1 page

Font styles to use
Sans Serif

Requirements
Must have
• easy to navigate friendly interface

```html
<!DOCTYPE html>
<html lang="en">
<head>
<meta charset="utf-8">
<title>Lomi-Seret</title>
<link href="https://fonts.googleapis.com/css2?family=Montserrat:wght@400;500;600;700&display=swap" rel="stylesheet">
<style>
:root{
  --navy:#1e2634;
  --red:#860000;
  --white:#ffffff;
  --text:#3a3a3a;
  --muted:#8a8f98;
  --foot-text:#aab0ba;
}
*{box-sizing:border-box;margin:0;padding:0}
html,body{width:1200px;height:2427px;overflow:hidden}
body{font-family:'Montserrat',sans-serif;color:var(--text);background:var(--white);position:relative}
.abs{position:absolute}
.topnav{left:0;top:0;width:1200px;height:47px;background:var(--navy)}
.topnav ul{list-style:none;display:flex;position:absolute;left:180px;top:0;height:47px}
.topnav li{font-size:10.5px;font-weight:700;color:var(--white);padding:0 13px;line-height:47px}
.topnav li.active{background:var(--white);color:var(--navy);padding:0 30px 0 23px}
.social{display:flex;gap:8px}
.social span{width:11px;height:11px;border-radius:50%;background:#6c7380;display:block}
.header{left:0;top:47px;width:1200px;height:109px;background:var(--white)}
.brand{left:180px;top:10px;display:flex;align-items:center;gap:8px}
.brand .mark{width:18px;height:18px;border-radius:50%;background:var(--red)}
.brand b{font-size:16px;font-weight:700;color:var(--red)}
.contact{display:flex;align-items:center;gap:12px}
.contact small{display:block;font-size:10px;color:var(--muted);margin-bottom:4px}
.contact strong{font-size:12px;font-weight:700;color:#111}
.divider{left:681px;top:40px;width:1px;height:34px;background:#ddd}
.btn-donate{left:880px;top:32px;width:137px;height:44px;background:var(--red);color:var(--white);font-size:12px;font-weight:700;display:flex;align-items:center;justify-content:center}
.hero{left:0;top:156px;width:1200px;height:538px;background:linear-gradient(100deg,#5a4c42 0%,#3d3330 30%,#2b2422 48%,#c9c4be 70%,#6d6a58 100%)}
.hero h2{left:180px;top:163px;font-size:27px;font-weight:600;color:var(--white)}
.hero h1{left:180px;top:200px;font-size:51px;font-weight:700;color:var(--white);letter-spacing:1px}
.btn-outline{border:2px solid var(--white);color:var(--white);font-size:12px;font-weight:700;display:flex;align-items:center;justify-content:center}
.welcome{left:0;top:694px;width:1200px;height:431px}
.welcome h3{position:absolute;top:62px;width:100%;text-align:center;font-size:25px;font-weight:700;color:var(--red)}
.welcome p{position:absolute;left:180px;width:840px;text-align:center;font-size:12.6px;line-height:19px;color:#444}
.welcome a{position:absolute;top:345px;width:100%;text-align:center;font-size:12px;font-weight:700;color:var(--red);text-decoration:none}
.news{left:0;top:1125px;width:1200px;height:672px;background:linear-gradient(90deg,#2c3442,#3e4656 45%,#2a3240)}
.news h3{position:absolute;top:60px;width:100%;text-align:center;font-size:25px;font-weight:700;color:var(--white)}
.card-img{width:240px;height:204px;top:145px}
.card{width:221px;height:240px;top:301px;background:var(--white);padding:24px 16px 0 16px}
.card .date{font-size:12px;color:#333;padding-left:2px}
.card h4{font-size:16.5px;font-weight:700;color:var(--red);line-height:19px;margin-top:14px;padding-left:2px}
.card p{font-size:12.6px;line-height:19px;color:#444;margin-top:21px}
.card a{display:block;font-size:12.6px;color:var(--red);margin-top:13px;text-decoration:none}
.subscribe{left:0;top:1797px;width:1200px;height:133px;background:var(--red)}
.subscribe h3{left:178px;top:45px;font-size:24px;font-weight:700;color:var(--white)}
.subscribe p{left:178px;top:85px;font-size:14.5px;color:var(--white)}
.sub-form{left:640px;top:47px;width:379px;height:44px;border:2px solid var(--white);display:flex}
.sub-form .field{flex:1;color:var(--white);font-size:14.5px;padding-left:14px;display:flex;align-items:center}
.sub-form .go{width:122px;background:var(--white);color:var(--red);font-size:12px;font-weight:700;display:flex;align-items:center;justify-content:center}
.partners{left:180px;top:1985px;width:840px;display:flex;justify-content:space-between;align-items:center}
.partners span{display:block;background:#d5d6d9}
.footer{left:0;top:2121px;width:1200px;height:306px;background:var(--navy)}
.footer h4{font-size:15.5px;font-weight:700;color:var(--white)}
.footer p{font-size:11.2px;line-height:19px;color:var(--foot-text)}
.ci{display:flex;gap:10px;font-size:11.2px;line-height:19px;color:var(--foot-text)}
.ci svg{flex:none;margin-top:3px}
.btn-support{left:881px;top:62px;width:137px;height:44px;background:var(--white);color:var(--red);font-size:12px;font-weight:700;display:flex;align-items:center;justify-content:center}
.foot-line{left:180px;top:258px;width:838px;height:1px;background:#3c4556}
.copy{left:180px;top:276px;font-size:11.2px;color:var(--foot-text)}
</style>
</head>
<body>

<nav class="abs topnav">
  <ul>
    <li class="active">HOME</li><li>ABOUT</li><li>THE COMMUNITY</li><li>PROGRAMS</li><li>NEWS</li><li>ADVOCACY</li><li>PARTNERS</li><li>SUPPORT US</li>
  </ul>
  <div class="abs social" style="left:954px;top:18px"><span></span><span></span><span></span></div>
</nav>

<header class="abs header">
  <div class="abs brand" style="top:45px"><span class="mark"></span><b>Lomi-Seret</b></div>
  <div class="abs contact" style="left:447px;top:41px">
    <svg width="22" height="17" viewBox="0 0 22 17"><rect width="22" height="17" rx="1" fill="#9a9ea6"/><path d="M0 1l11 8 11-8" stroke="#fff" stroke-width="2" fill="none"/></svg>
    <div><small>EMAIL US AT</small><strong>LOMISERET@EXAMPLE.ORG</strong></div>
  </div>
  <div class="abs divider"></div>
  <div class="abs contact" style="left:720px;top:41px">
    <svg width="20" height="20" viewBox="0 0 24 24"><path d="M6.6 10.8a15 15 0 006.6 6.6l2.2-2.2a1 1 0 011-.25 11.4 11.4 0 003.6.6 1 1 0 011 1V20a1 1 0 01-1 1A17 17 0 013 4a1 1 0 011-1h3.5a1 1 0 011 1 11.4 11.4 0 00.6 3.6 1 1 0 01-.25 1z" fill="#9a9ea6"/></svg>
    <div><small>CALL US NOW</small><strong>04-5550182</strong></div>
  </div>
  <div class="abs btn-donate">DONATE NOW</div>
</header>

<section class="abs hero" role="img" aria-label="Photograph of a mother carrying her young daughter wrapped in a white shawl">
  <h2 class="abs">WELCOME TO</h2>
  <h1 class="abs">LOMI-SERET</h1>
  <div class="abs btn-outline" style="left:180px;top:289px;width:137px;height:44px">READ MORE</div>
</section>

<section class="abs welcome">
  <h3>WELCOME TO LOMI SERET</h3>
  <p style="top:129px">Aliyah (immigration) from Ethiopia to Israel and the transition to a sedentary lifestyle has resulted in the emergence of chronic diseases, in particular diabetes. While only 0.4% of the new immigrants were diagnosed with Type 2 diabetes upon arrival, by the time they had lived in Israel for ten years the figure had risen to 18% - three times as many as in the general population.  The incidence of hypertension, obesity, asthma and Type 1 diabetes had also increased dramatically.</p>
  <p style="top:223px">Lomi Seret was founded in 1999 by Dr. Miriam Halevi, Head of the Endocrinology Unit at the Carmel Vale Medical Center. Her experience with Ethiopian patients made her realize that medical treatment could not succeed without culturally competent communication.  Lomi Seret has developed into a small but dedicated NGO, delivering services throughout Israel with the backing and cooperation of a wide range of local and national bodies, including the Ministry of Health, the Ministry of Immigration, the absorption services, municipalities, the HMOs and hospitals.</p>
  <a href="#">READ MORE..</a>
</section>

<section class="abs news" role="img" aria-label="Darkened photograph of community members seated in a group meeting">
  <h3>LATEST NEWS</h3>
  <div class="abs card-img" style="left:179px;background:linear-gradient(160deg,#8a6a5a,#b89a8a 45%,#6f8a4a)" role="img" aria-label="Photograph of two smiling children"></div>
  <div class="abs card-img" style="left:479px;background:linear-gradient(180deg,#e8e8ea,#d9d2cc 60%,#c7bfb6)" role="img" aria-label="Photograph of a doctor holding a patient's hands"></div>
  <div class="abs card-img" style="left:778px;background:linear-gradient(160deg,#8a6a5a,#b89a8a 45%,#6f8a4a)" role="img" aria-label="Photograph of two smiling children"></div>
  <article class="abs card" style="left:188px"><div class="date">November 17, 2021</div><h4>Lorem Ipsum is simply dummy text</h4><p>Lorem Ipsum has been the industry's standard dummy text ever since the 1500s, when an unknown printer.</p><a href="#">Read more..</a></article>
  <article class="abs card" style="left:488px"><div class="date">November 17, 2021</div><h4>Lorem Ipsum is simply dummy text</h4><p>Lorem Ipsum has been the industry's standard dummy text ever since the 1500s, when an unknown printer.</p><a href="#">Read more..</a></article>
  <article class="abs card" style="left:787px"><div class="date">November 17, 2021</div><h4>Lorem Ipsum is simply dummy text</h4><p>Lorem Ipsum has been the industry's standard dummy text ever since the 1500s, when an unknown printer.</p><a href="#">Read more..</a></article>
  <div class="abs btn-outline" style="left:532px;top:593px;width:137px;height:44px">VIEW ALL NEWS</div>
</section>

<section class="abs subscribe">
  <h3 class="abs">SUBSCRIBE TO NEWSLETTER</h3>
  <p class="abs">Sign up with your email address to receive news and updates</p>
  <div class="abs sub-form"><div class="field">Your email address..</div><div class="go">SUBSCRIBE</div></div>
</section>

<div class="abs partners" aria-label="Partner organisations">
  <span style="width:58px;height:58px"></span>
  <span style="width:96px;height:22px"></span>
  <span style="width:86px;height:48px"></span>
  <span style="width:78px;height:52px"></span>
  <span style="width:46px;height:70px"></span>
  <span style="width:84px;height:30px"></span>
</div>

<footer class="abs footer">
  <div class="abs" style="left:180px;top:60px;width:200px"><h4>ABOUT US</h4><p style="margin-top:22px">Lomi Seret (“health” in both Amharic and Hebrew) is dedicated to improving the health of the Ethiopian Israeli community.</p></div>
  <div class="abs" style="left:395px;top:60px;width:200px"><h4>OUR PROGRAMS</h4><p style="margin-top:22px">Lomi Seret (“health” in both Amharic and Hebrew) is dedicated to improving the health of the Ethiopian Israeli community.</p></div>
  <div class="abs" style="left:625px;top:60px;width:250px">
    <h4>CONTACT US</h4>
    <div class="ci" style="margin-top:22px"><svg width="13" height="13" viewBox="0 0 24 24"><path d="M6.6 10.8a15 15 0 006.6 6.6l2.2-2.2a1 1 0 011-.25 11.4 11.4 0 003.6.6 1 1 0 011 1V20a1 1 0 01-1 1A17 17 0 013 4a1 1 0 011-1h3.5a1 1 0 011 1 11.4 11.4 0 00.6 3.6 1 1 0 01-.25 1z" fill="#8a909a"/></svg><div>PHONE<br>04-5550182</div></div>
    <div class="ci"><svg width="13" height="15" viewBox="0 0 12 16"><path d="M6 0a6 6 0 00-6 6c0 4.5 6 10 6 10s6-5.5 6-10a6 6 0 00-6-6zm0 8.5A2.5 2.5 0 116 3.5a2.5 2.5 0 010 5z" fill="#8a909a"/></svg><div>OFFICE<br>Kfar Lev 12/4 POB 2210 Galil, 40215</div></div>
    <div class="ci"><svg width="13" height="10" viewBox="0 0 22 17"><rect width="22" height="17" fill="#8a909a"/><path d="M0 1l11 8 11-8" stroke="#1e2634" stroke-width="2" fill="none"/></svg><div>EMAIL<br>lomiseret@example.org</div></div>
  </div>
  <div class="abs btn-support">SUPPORT US</div>
  <div class="abs foot-line"></div>
  <div class="abs copy">Privacy Policy &nbsp;I&nbsp; Copyright © 2022 / All Rights Reserved</div>
  <div class="abs social" style="left:955px;top:279px"><span></span><span></span><span></span></div>
</footer>

</body>
</html>
```